I need a new design for my real estate signage!

Would like a new design for my real estate signs. I do have a logo that needs to be used along with the word AVAILABLE and my phone number 505-718-2094

Target Market(s)

Real estate buyers and sellers

Industry/Entity Type

Real Estate

Font styles to use
Serif

Colors
000000

Requirements
Must have
• Company name phone number
• Colors: turquoise, white black
Nice to have
• Modern design

```html
<!DOCTYPE html>
<html lang="en">
<head>
<meta charset="utf-8">
<title>Valdera Real Estate Services – Available Sign</title>
<link rel="stylesheet" href="https://fonts.googleapis.com/css2?family=Cinzel:wght@500&family=Josefin+Sans:wght@600&family=Arimo:wght@700&display=swap">
<style>
  :root {
    --sign-black: #060809;
    --turquoise: #1b8fa0;
    --turquoise-deep: #157586;
    --name-teal: #1a7f8e;
    --tagline-grey: #5c5d5f;
    --silver-light: #f2f3f4;
    --silver-dark: #8e9296;
    --white: #ffffff;
  }
  html, body {
    margin: 0;
    padding: 0;
    width: 900px;
    height: 1200px;
    overflow: hidden;
    background: var(--sign-black);
  }
  .sign {
    display: block;
    width: 900px;
    height: 1200px;
  }
  .brand-mark {
    fill: var(--name-teal);
  }
  .brand-name {
    font-family: "Cinzel", "Trajan Pro", serif;
    font-weight: 500;
    fill: var(--name-teal);
  }
  .brand-tagline {
    font-family: "Josefin Sans", "Futura", sans-serif;
    font-weight: 600;
    fill: var(--tagline-grey);
  }
  .sale-heading,
  .sale-phone {
    font-family: "Arimo", "Helvetica Neue", Arial, sans-serif;
    font-weight: 700;
    fill: var(--white);
  }
</style>
</head>
<body>
  <svg class="sign" viewBox="0 0 900 1200" xmlns="http://www.w3.org/2000/svg" aria-label="Valdera Real Estate Services available sign">
    <defs>
      <linearGradient id="silver-band" x1="0" y1="0" x2="1" y2="0">
        <stop offset="0" stop-color="var(--silver-dark)"/>
        <stop offset="0.5" stop-color="var(--silver-light)"/>
        <stop offset="1" stop-color="var(--silver-dark)"/>
      </linearGradient>
      <linearGradient id="turquoise-panel" x1="0" y1="0" x2="0" y2="1">
        <stop offset="0" stop-color="var(--turquoise)"/>
        <stop offset="1" stop-color="var(--turquoise-deep)"/>
      </linearGradient>
    </defs>

    <rect class="sign-field" width="900" height="1200" fill="var(--sign-black)"/>

    <g class="brand">
      <rect class="brand-mark" x="300" y="130" width="300" height="300" aria-hidden="true"/>
      <text class="brand-name" x="450" y="665" font-size="150" text-anchor="middle" textLength="723" lengthAdjust="spacingAndGlyphs">VALDERA</text>
      <text class="brand-tagline" x="450" y="720" font-size="38" text-anchor="middle" textLength="716" lengthAdjust="spacing">REAL ESTATE SERVICES</text>
    </g>

    <path class="silver-band" d="M0,859 Q450,709 900,859 L900,875 Q450,725 0,875 Z" fill="url(#silver-band)"/>
    <path class="sale-panel" d="M0,873 Q450,723 900,873 L900,1200 L0,1200 Z" fill="url(#turquoise-panel)"/>

    <g class="sale-info">
      <text class="sale-heading" x="452" y="1030" font-size="140" text-anchor="middle" textLength="688" lengthAdjust="spacingAndGlyphs">AVAILABLE</text>
      <text class="sale-phone" x="452" y="1144" font-size="120" text-anchor="middle" textLength="689" lengthAdjust="spacingAndGlyphs">505-718-2094</text>
    </g>
  </svg>
</body>
</html>
```